Coffee roasting needs homepage with web shop

small roasting (no cafe!) needs a simple website with a web shop. We sell coffee to dealers and end customers. The shop should be for end consumers as well as for B2B customers. A login should be available. The design should be modern and at the same time classic with subtle (dark) colors. We need the tabs "Coffee, Shop, Contact, Coffee, Coffee, Login, About Us, Imprint, Privacy" Logo nr 1 should be used from attached file

Target Market(s)

B2B

Number of Pages Required

5+ page

Font styles to use
Sans Serif

Colors

Designer to choose only greyscale colors for use in the design.

Requirements
Must have
• Webshop

```html
<!DOCTYPE html>
<html lang="en">
<head>
<meta charset="utf-8">
<title>Bohnwerk – Coffee Roasters</title>
<link href="https://fonts.googleapis.com/css2?family=Montserrat:wght@300;400;500;600;700&family=Open+Sans:wght@400;600&display=swap" rel="stylesheet">
<style>
:root{
  --espresso:#34211a;
  --espresso-deep:#2a1a13;
  --roast:#5b2c12;
  --ink:#222;
  --paper:#fff;
  --mist:#f1f1f1;
  --line:#ddd;
  --star:#e0762b;
}
*{box-sizing:border-box;margin:0;padding:0}
html,body{width:1200px;height:4800px;overflow:hidden}
body{position:relative;font-family:"Open Sans",Arial,sans-serif;color:var(--ink);background:var(--paper)}
.abs{position:absolute}

/* hero */
.hero{left:0;top:0;width:1200px;height:667px;background:#3a2418}
.hero .photo{left:0;top:0;width:1200px;height:667px}
.brand{left:144px;top:86px;display:flex;align-items:center;gap:12px;color:#fff;font:500 28px "Montserrat",sans-serif}
.brand i{display:block;width:22px;height:22px;border-radius:50%;background:#fff}
.nav{left:405px;top:98px;display:flex;gap:23px;font-family:"Montserrat",sans-serif;font-weight:600;font-size:16px;color:#fff}
.login{left:866px;top:36px;width:96px;height:34px;background:var(--roast);color:#fff;font:500 14px "Montserrat",sans-serif;display:flex;align-items:center;justify-content:center}
.hero-title{left:560px;top:252px;width:540px;text-align:center;font:400 90px/1 "Montserrat",sans-serif;color:#fff}
.hero-text{left:560px;top:372px;width:540px;text-align:center;font-size:17px;line-height:30px;color:#fff}
.btn-dark{background:#111;color:#fff;font:600 15px "Montserrat",sans-serif;display:flex;align-items:center;justify-content:center}
.hero .btn-dark{left:740px;top:454px;width:182px;height:46px}
.arrow{width:30px;height:30px;border-radius:50%;display:flex;align-items:center;justify-content:center}

.section-title{left:0;width:1200px;text-align:center;font:400 34px "Montserrat",sans-serif}
.section-title b{font-weight:600}
.rule{width:72px;height:3px;background:#fff;left:564px}

/* coffee cards */
.cat-card{top:827px;width:294px;height:419px;background:var(--roast)}
.cat-card .img{left:0;top:0;width:294px;height:176px}
.cat-card .dot{left:120px;top:146px;width:56px;height:56px;border-radius:50%;background:#fff;border:4px solid var(--roast)}
.cat-card .dot::after{content:"";position:absolute;left:14px;top:12px;width:20px;height:24px;border-radius:50%;background:var(--roast)}
.cat-card h3{left:0;top:240px;width:294px;text-align:center;font:500 16px "Montserrat",sans-serif;color:#fff}
.cat-card p{left:20px;top:270px;width:254px;text-align:center;font-size:12.5px;line-height:24px;color:#f3e6dd}
.cat-card .btn-dark{left:86px;top:358px;width:122px;height:32px;font-size:12px}

/* products */
.band-dark{left:0;width:1200px;background:var(--espresso)}
.prod{top:1548px;width:214px;height:255px;background:#fff;border:3px solid #fff}
.prod .img{left:0;top:0;width:208px;height:249px}
.prod-name{width:214px;text-align:center;color:#fff;font-size:16px;line-height:26px;top:1818px}
.prod-price{width:214px;text-align:center;color:#fff;font:italic 600 16px "Open Sans",sans-serif;top:1876px}
.ring-arrow{width:26px;height:26px;border:1.5px solid #fff;border-radius:50%;display:flex;align-items:center;justify-content:center}

/* welcome */
.welcome-h{left:143px;top:2078px;font:500 36px "Montserrat",sans-serif}
.welcome-name{left:143px;top:2130px;font:400 60px "Montserrat",sans-serif}
.welcome-p{left:143px;top:2222px;width:370px;font-size:14px;line-height:30px;color:#444}
.welcome-bean{left:300px;top:2250px;width:200px;height:190px;border-radius:50%;background:radial-gradient(circle,#f0ece8,#fff 70%)}
.btn-outline{left:143px;top:2396px;width:133px;height:38px;border:1.5px solid #222;border-radius:5px;font:600 14px "Montserrat",sans-serif;display:flex;align-items:center;justify-content:center}
.feature h4{font:600 15px/21px "Montserrat",sans-serif;color:#222;position:absolute;left:56px;top:4px;width:170px}
.feature p{position:absolute;left:0;top:58px;width:220px;font-size:12.5px;line-height:24px;color:#555}
.feature svg{position:absolute;left:0;top:0}

/* news */
.news{top:2735px;width:284px;height:341px;background:#fff}
.news .img{left:0;top:0;width:284px;height:184px}
.news .date{left:74px;top:170px;width:136px;height:28px;background:var(--roast);color:#fff;font-size:12px;display:flex;align-items:center;justify-content:center}
.news h3{left:0;top:218px;width:284px;text-align:center;font:400 17px "Open Sans",sans-serif;color:#333}
.news p{left:20px;top:254px;width:244px;text-align:center;font-size:12px;line-height:22px;color:#444}

/* deal */
.deal-box{left:143px;top:3298px;width:913px;height:488px;border:1px solid var(--line)}
.deal-col{top:3299px;width:228px;height:486px}
.deal-col.shade{background:var(--mist)}
.deal-badge{left:458px;top:3266px;width:282px;height:60px;background:var(--roast);color:#fff;font:500 24px "Montserrat",sans-serif;display:flex;align-items:center;justify-content:center}
.deal-img{top:3362px;width:160px;height:250px}
.deal-off{top:3386px;width:40px;height:40px;border-radius:50%;background:var(--roast);color:#fff;font-size:13px;display:flex;align-items:center;justify-content:center}
.stars{top:3630px;width:228px;text-align:center;color:var(--star);font-size:13px;letter-spacing:1px}
.deal-name{top:3654px;width:228px;text-align:center;font-size:16px;line-height:27px;color:#333}
.deal-price{top:3722px;width:228px;text-align:center;font-size:16px;color:var(--roast);font-weight:600}

/* service + newsletter */
.service{left:0;top:3884px;width:1200px;height:438px;background:linear-gradient(90deg,#e9e9e9 0%,#f7f7f7 20%,#f7f7f7 80%,#e9e9e9 100%)}
.srv h4{position:absolute;left:62px;top:0;font:600 16px "Montserrat",sans-serif;color:#222;white-space:nowrap}
.srv p{position:absolute;left:62px;top:28px;font-size:11.5px;color:#444;white-space:nowrap}
.srv svg{position:absolute;left:0;top:0}
.nl-title{left:0;top:4102px;width:1200px;text-align:center;font:600 32px "Montserrat",sans-serif;color:#222}
.nl-text{left:0;top:4160px;width:1200px;text-align:center;font-size:14.5px;line-height:24px;color:#333}
.nl-form{left:347px;top:4225px;width:504px;height:38px;border:1px solid #ccc;border-radius:19px;background:#fff;overflow:hidden}
.nl-form span{position:absolute;left:20px;top:12px;font-size:10px;color:#555}
.nl-form b{position:absolute;right:0;top:0;width:118px;height:38px;background:var(--roast);color:#fff;font:500 14px "Montserrat",sans-serif;display:flex;align-items:center;justify-content:center}

/* footer */
.footer{left:0;top:4322px;width:1200px;height:478px;background:var(--espresso-deep)}
.f-head{top:4402px;font:500 18px "Montserrat",sans-serif;color:#fff}
.f-list{list-style:none;color:#ddd;font-size:12.5px}
.f-list li{height:29px}
.f-list li::before{content:"›";margin-right:10px;color:#bbb}
.contact-row{left:143px;color:#ddd;font-size:12.5px;line-height:20px}
.contact-row svg{position:absolute;left:0;top:2px}
.contact-row div{position:absolute;left:36px;top:0;width:260px}
.f-mark{left:1010px;top:4582px;color:#5b4a41;font:400 24px "Montserrat",sans-serif}
.f-rule{left:143px;top:4712px;width:913px;height:1px;background:#4a3a32}
.copy{left:143px;top:4742px;color:#ddd;font-size:12.5px}
.social{top:4732px;width:34px;height:34px;border:1.5px solid #ccc;border-radius:50%}
.card{top:4740px;width:36px;height:22px;border-radius:3px}
</style>
</head>
<body>

<section class="abs hero">
  <div class="abs photo" role="img" aria-label="Roasted coffee beans falling onto a pile of beans" style="background:radial-gradient(ellipse at 28% 40%,#7a4828,#4a2a18 50%,#1e110b 100%)"></div>
  <div class="abs brand"><i></i><span>Bohnwerk</span></div>
  <div class="abs login">LOGIN</div>
  <svg class="abs" style="left:982px;top:40px" width="30" height="28" viewBox="0 0 30 28"><path d="M4 8h20l-2 16H6z" fill="none" stroke="#fff" stroke-width="2"/><path d="M9 8a5 5 0 0 1 10 0" fill="none" stroke="#fff" stroke-width="2"/><circle cx="25" cy="6" r="5" fill="#fff"/></svg>
  <svg class="abs" style="left:1034px;top:44px" width="20" height="20" viewBox="0 0 20 20"><circle cx="8" cy="8" r="6" fill="none" stroke="#fff" stroke-width="2.5"/><path d="M12.5 12.5L18 18" stroke="#fff" stroke-width="2.5"/></svg>
  <div class="abs" style="left:424px;top:68px;width:14px;height:18px;border:2px solid #fff;border-radius:50%"></div>
  <nav class="abs nav"><span>HOME</span><span>COFFEE</span><span>SHOP</span><span>ABOUT US</span><span>IMPRINT</span><span>PRIVACY</span><span>CONTACT</span></nav>
  <div class="abs hero-title">Bohnwerk</div>
  <p class="abs hero-text">Sed ut perspiciatis unde omnis iste natus<br>sit voluptatem accusantium doloremque laudantium</p>
  <div class="abs btn-dark">SHOP NOW</div>
  <div class="abs arrow" style="left:82px;top:320px;background:#111"><svg width="10" height="12"><path d="M7 1L2 6l5 5" stroke="#fff" stroke-width="2" fill="none"/></svg></div>
  <div class="abs arrow" style="left:1088px;top:320px;background:#111"><svg width="10" height="12"><path d="M3 1l5 5-5 5" stroke="#fff" stroke-width="2" fill="none"/></svg></div>
</section>

<h2 class="abs section-title" style="top:736px;color:#222">Bohnwerk <b>Coffee</b></h2>
<article class="abs cat-card" style="left:143px">
  <div class="abs img" role="img" aria-label="Scoop of roasted beans spilling from a burlap sack" style="background:linear-gradient(135deg,#2e2925,#6b4a32 60%,#3a2a20)"></div>
  <div class="abs dot"></div>
  <h3 class="abs">NEMO ENIM IPSAM</h3>
  <p class="abs">Sed ut perspiciatis unde omnis iste natus error sit voluptatem accusantium doloremque laudantium, totam</p>
  <div class="abs btn-dark">SHOP NOW</div>
</article>
<article class="abs cat-card" style="left:453px">
  <div class="abs img" role="img" aria-label="Close-up of coffee beans on ground coffee" style="background:linear-gradient(180deg,#2a2422,#5a3a2a 55%,#8a4a2a)"></div>
  <div class="abs dot"></div>
  <h3 class="abs">NEMO ENIM IPSAM</h3>
  <p class="abs">Sed ut perspiciatis unde omnis iste natus error sit voluptatem accusantium doloremque laudantium, totam</p>
  <div class="abs btn-dark">SHOP NOW</div>
</article>
<article class="abs cat-card" style="left:762px">
  <div class="abs img" role="img" aria-label="Coffee cup in front of a plantation at sunset" style="background:linear-gradient(180deg,#f0a040,#c27a2a 45%,#4a5a22 80%,#3a3a1a)"></div>
  <div class="abs dot"></div>
  <h3 class="abs">NEMO ENIM IPSAM</h3>
  <p class="abs">Sed ut perspiciatis unde omnis iste natus error sit voluptatem accusantium doloremque laudantium, totam</p>
  <div class="abs btn-dark">SHOP NOW</div>
</article>

<section class="abs band-dark" style="top:1341px;height:649px"></section>
<h2 class="abs section-title" style="top:1420px;color:#fff">Bohnwerk <b>Products</b></h2>
<div class="abs rule" style="top:1486px"></div>
<div class="abs ring-arrow" style="left:87px;top:1672px"><svg width="8" height="10"><path d="M6 1L2 5l4 4" stroke="#fff" stroke-width="1.5" fill="none"/></svg></div>
<div class="abs ring-arrow" style="left:1087px;top:1672px"><svg width="8" height="10"><path d="M2 1l4 4-4 4" stroke="#fff" stroke-width="1.5" fill="none"/></svg></div>

<div class="abs prod" style="left:143px"><div class="abs img" role="img" aria-label="Kraft coffee box packaging" style="background:linear-gradient(135deg,#fff,#f2ece4 40%,#d8b98a 60%,#fff)"></div></div>
<div class="abs prod" style="left:376px"><div class="abs img" role="img" aria-label="Brown paper coffee bag with beans" style="background:linear-gradient(180deg,#fff,#c89a66 30%,#a8784a 80%,#fff)"></div></div>
<div class="abs prod" style="left:609px"><div class="abs img" role="img" aria-label="White paper coffee bag with label" style="background:linear-gradient(180deg,#fff,#eee8dc 30%,#d9d0c0 80%,#fff)"></div></div>
<div class="abs prod" style="left:842px"><div class="abs img" role="img" aria-label="Glass jar of instant coffee" style="background:linear-gradient(180deg,#fff 5%,#222 20%,#5a2a10 55%,#2a1a10 85%,#fff)"></div></div>

<p class="abs prod-name" style="left:143px">Sed ut perspiciatis unde<br>omnis iste natus</p>
<p class="abs prod-name" style="left:376px">Sed ut perspiciatis unde<br>omnis iste natus</p>
<p class="abs prod-name" style="left:609px">Sed ut perspiciatis unde<br>omnis iste natus</p>
<p class="abs prod-name" style="left:842px">Sed ut perspiciatis unde<br>omnis iste natus</p>
<p class="abs prod-price" style="left:143px">$49.95</p>
<p class="abs prod-price" style="left:376px">$49.95</p>
<p class="abs prod-price" style="left:609px">$49.95</p>
<p class="abs prod-price" style="left:842px">$49.95</p>

<div class="abs welcome-bean" role="img" aria-label="Faint sketch of coffee beans"></div>
<h2 class="abs welcome-h">Welcome to</h2>
<div class="abs welcome-name">Bohnwerk</div>
<p class="abs welcome-p">Sed ut perspiciatis unde omnis iste natus error sit voluptatem accusantium doloremque laudantium, totam rem aperiam, eaque ipsa quae ab illo inventore veritatis et quasi architecto beatae vitae dicta sunt explicabo. Nemo enim ipsam</p>
<div class="abs btn-outline">READ MORE</div>

<div class="abs feature" style="left:568px;top:2090px;width:230px;height:150px">
  <svg width="44" height="54" viewBox="0 0 44 54"><ellipse cx="22" cy="30" rx="14" ry="20" transform="rotate(25 22 30)" fill="none" stroke="#333" stroke-width="2"/><path d="M14 44c8-8 6-20 16-28" fill="none" stroke="#333" stroke-width="2"/></svg>
  <h4>THE BEST WORLD SORTS</h4>
  <p>Sed ut perspiciatis unde omnis iste natus error sit voluptatem antium doloremque laudantium, totam</p>
</div>
<div class="abs feature" style="left:842px;top:2090px;width:230px;height:150px">
  <svg width="46" height="46" viewBox="0 0 46 46"><path d="M3 16h40M3 16l4-12h32l4 12v26H3z" fill="none" stroke="#333" stroke-width="2"/><rect x="9" y="24" width="10" height="18" fill="none" stroke="#333" stroke-width="2"/><rect x="25" y="24" width="12" height="9" fill="none" stroke="#333" stroke-width="2"/></svg>
  <h4>MANY POINTS OF SALE</h4>
  <p>Sed ut perspiciatis unde omnis iste natus error sit voluptatem antium doloremque laudantium, totam</p>
</div>
<div class="abs feature" style="left:568px;top:2266px;width:230px;height:150px">
  <svg width="44" height="50" viewBox="0 0 44 50"><rect x="3" y="3" width="38" height="44" fill="none" stroke="#333" stroke-width="2"/><path d="M3 14h38" stroke="#333" stroke-width="2"/><rect x="12" y="22" width="20" height="16" fill="none" stroke="#333" stroke-width="2"/></svg>
  <h4>PROFESSIONAL BARISTAS</h4>
  <p>Sed ut perspiciatis unde omnis iste natus error sit voluptatem antium doloremque laudantium, totam</p>
</div>
<div class="abs feature" style="left:842px;top:2266px;width:230px;height:150px">
  <svg width="54" height="46" viewBox="0 0 54 46"><path d="M3 8h30v26H3zM33 16h10l8 10v8H33" fill="none" stroke="#333" stroke-width="2"/><circle cx="12" cy="36" r="5" fill="#fff" stroke="#333" stroke-width="2"/><circle cx="42" cy="36" r="5" fill="#fff" stroke="#333" stroke-width="2"/></svg>
  <h4>24/7 FAST DELIVERY</h4>
  <p>Sed ut perspiciatis unde omnis iste natus error sit voluptatem antium doloremque laudantium, totam</p>
</div>

<section class="abs band-dark" style="top:2534px;height:642px"></section>
<h2 class="abs section-title" style="top:2609px;color:#fff">Bohnwerk <b>Latest News</b></h2>
<div class="abs rule" style="top:2676px"></div>
<div class="abs ring-arrow" style="left:93px;top:2870px"><svg width="8" height="10"><path d="M6 1L2 5l4 4" stroke="#fff" stroke-width="1.5" fill="none"/></svg></div>
<div class="abs ring-arrow" style="left:1093px;top:2870px"><svg width="8" height="10"><path d="M2 1l4 4-4 4" stroke="#fff" stroke-width="1.5" fill="none"/></svg></div>

<article class="abs news" style="left:143px">
  <div class="abs img" role="img" aria-label="Person enjoying a cup of coffee in a cafe" style="background:linear-gradient(135deg,#3a2a20,#7a5a44 50%,#d8d0c8)"></div>
  <div class="abs date">▦ October 17, 2019</div>
  <h3 class="abs">Quis autem vel eum iure</h3>
  <p class="abs">Sed ut perspiciatis unde omnis iste natus error sit voluptatem accusantium doloremque lauantium</p>
</article>
<article class="abs news" style="left:456px">
  <div class="abs img" role="img" aria-label="Coffee beans and green leaves on a wooden table" style="background:linear-gradient(135deg,#2a4a44,#4a2a1a 45%,#2a3a2a)"></div>
  <div class="abs date">▦ October 17, 2019</div>
  <h3 class="abs">Quis autem vel eum iure</h3>
  <p class="abs">Sed ut perspiciatis unde omnis iste natus error sit voluptatem accusantium doloremque lauantium</p>
</article>
<article class="abs news" style="left:773px">
  <div class="abs img" role="img" aria-label="Hands holding freshly picked red coffee cherries" style="background:linear-gradient(135deg,#2a5a2a,#8a2a2a 50%,#3a6a2a)"></div>
  <div class="abs date">▦ October 17, 2019</div>
  <h3 class="abs">Quis autem vel eum iure</h3>
  <p class="abs">Sed ut perspiciatis unde omnis iste natus error sit voluptatem accusantium doloremque lauantium</p>
</article>

<div class="abs deal-box"></div>
<div class="abs deal-col" style="left:144px"></div>
<div class="abs deal-col shade" style="left:372px"></div>
<div class="abs deal-col" style="left:600px"></div>
<div class="abs deal-col shade" style="left:828px"></div>
<div class="abs deal-badge">DEAL OF THE WEEK</div>
<div class="abs ring-arrow" style="left:72px;top:3530px;border-color:#555;width:34px;height:34px"><svg width="8" height="10"><path d="M6 1L2 5l4 4" stroke="#555" stroke-width="1.5" fill="none"/></svg></div>
<div class="abs ring-arrow" style="left:1090px;top:3530px;border-color:#555;width:34px;height:34px"><svg width="8" height="10"><path d="M2 1l4 4-4 4" stroke="#555" stroke-width="1.5" fill="none"/></svg></div>

<div class="abs deal-img" style="left:178px;background:linear-gradient(180deg,#d8b68a,#b88a5a 60%,#9a7048)" role="img" aria-label="Kraft coffee bag with window showing beans"></div>
<div class="abs deal-img" style="left:406px;background:linear-gradient(180deg,#bbb 0,#888 14%,#8a4a24 18%,#6a3418 70%,#4a2410)" role="img" aria-label="Jar of ground coffee with silver lid"></div>
<div class="abs deal-img" style="left:634px;background:linear-gradient(180deg,#a0784e,#8a6038 60%,#6a4828)" role="img" aria-label="Brown paper coffee bag"></div>
<div class="abs deal-img" style="left:862px;background:linear-gradient(180deg,#5a3a24,#3a2416 60%,#2a1a10)" role="img" aria-label="Clear bag filled with roasted coffee beans"></div>

<div class="abs deal-off" style="left:312px">10%</div>
<div class="abs deal-off" style="left:536px">10%</div>
<div class="abs deal-off" style="left:768px">10%</div>
<div class="abs deal-off" style="left:992px">10%</div>

<div class="abs stars" style="left:144px">★★★★☆</div>
<div class="abs stars" style="left:372px">★★★★☆</div>
<div class="abs stars" style="left:600px">★★★★☆</div>
<div class="abs stars" style="left:828px">★★★★☆</div>
<p class="abs deal-name" style="left:144px">Nemo enim ipsam<br>voluptatem quia voluptas</p>
<p class="abs deal-name" style="left:372px">Nemo enim ipsam<br>voluptatem quia voluptas</p>
<p class="abs deal-name" style="left:600px">Nemo enim ipsam<br>voluptatem quia voluptas</p>
<p class="abs deal-name" style="left:828px">Nemo enim ipsam<br>voluptatem quia voluptas</p>
<p class="abs deal-price" style="left:144px">$ 5.42</p>
<p class="abs deal-price" style="left:372px">$ 5.42</p>
<p class="abs deal-price" style="left:600px">$ 5.42</p>
<p class="abs deal-price" style="left:828px">$ 5.42</p>

<section class="abs service" role="img" aria-label="Sketched coffee branches and beans framing the newsletter area"></section>
<div class="abs srv" style="left:336px;top:3942px">
  <svg width="46" height="40" viewBox="0 0 46 40"><rect x="4" y="8" width="34" height="26" rx="2" fill="none" stroke="#555" stroke-width="2"/><path d="M12 20h20M16 15l-5 5 5 5" fill="none" stroke="#555" stroke-width="2"/></svg>
  <h4>FREE RETURNS</h4><p>Duis aute irure dolor in</p>
</div>
<div class="abs srv" style="left:590px;top:3942px">
  <svg width="46" height="40" viewBox="0 0 46 40"><path d="M8 24v-6a15 15 0 0 1 30 0v6" fill="none" stroke="#555" stroke-width="2"/><rect x="5" y="22" width="8" height="12" fill="none" stroke="#555" stroke-width="2"/><rect x="33" y="22" width="8" height="12" fill="none" stroke="#555" stroke-width="2"/></svg>
  <h4>ONLINE SUPPORT</h4><p>Lorem ipsum dolor sit amet</p>
</div>
<div class="abs srv" style="left:328px;top:4014px">
  <svg width="54" height="40" viewBox="0 0 54 40"><rect x="3" y="8" width="48" height="26" rx="3" fill="none" stroke="#555" stroke-width="2"/><circle cx="27" cy="21" r="7" fill="none" stroke="#555" stroke-width="2"/></svg>
  <h4 style="left:74px">EASY PAYMENT</h4><p style="left:74px">For purchases from 499</p>
</div>
<div class="abs srv" style="left:596px;top:4014px">
  <svg width="46" height="40" viewBox="0 0 46 40"><circle cx="20" cy="20" r="16" fill="none" stroke="#555" stroke-width="2"/><circle cx="20" cy="20" r="7" fill="none" stroke="#555" stroke-width="2"/></svg>
  <h4 style="left:60px">48 HRS SHIPPING</h4><p style="left:60px">V / booking before kl. 16.30 Mon-Fri</p>
</div>
<h2 class="abs nl-title">JOIN OUR NEWSLETTER</h2>
<p class="abs nl-text">Subscribe to our mailing list to receive updates<br>and promotional offers.</p>
<div class="abs nl-form"><span>Enter your E - mail</span><b>SUBSCRIBE</b></div>

<footer class="abs footer"></footer>
<h4 class="abs f-head" style="left:143px">CONTACT US</h4>
<h4 class="abs f-head" style="left:475px">QUICK LINKS</h4>
<h4 class="abs f-head" style="left:681px">CUSTOMER SERVICE</h4>
<h4 class="abs f-head" style="left:921px">MY ACCOUNT</h4>

<div class="abs contact-row" style="top:4456px">
  <svg width="18" height="22" viewBox="0 0 18 22"><path d="M9 21s7-8 7-13a7 7 0 0 0-14 0c0 5 7 13 7 13z" fill="#fff"/><circle cx="9" cy="8" r="3" fill="#2a1a13"/></svg>
  <div style="font-size:11.5px">ADDRESS<br>45 Mill Lane, Townsville, England</div>
</div>
<div class="abs contact-row" style="top:4510px">
  <svg width="18" height="18" viewBox="0 0 18 18"><path d="M3 1h4l2 5-3 2a11 11 0 0 0 4 4l2-3 5 2v4c-8 1-15-6-14-14z" fill="#fff"/></svg>
  <div>Phone: (555) 014-2290</div>
</div>
<div class="abs contact-row" style="top:4543px">
  <svg width="18" height="14" viewBox="0 0 18 14"><rect x="1" y="1" width="16" height="12" fill="#fff"/><path d="M1 1l8 7 8-7" fill="none" stroke="#2a1a13" stroke-width="1.5"/></svg>
  <div>E-mail: info@bohnwerk.example</div>
</div>
<div class="abs contact-row" style="top:4576px">
  <svg width="18" height="18" viewBox="0 0 18 18"><circle cx="9" cy="9" r="8" fill="#fff"/><path d="M9 4v5h4" stroke="#2a1a13" stroke-width="1.8" fill="none"/></svg>
  <div>Opening hours:<br>Mon-Thurs: 9.30-17.30<br>Fri: 9.30-18.00</div>
</div>

<ul class="abs f-list" style="left:475px;top:4450px"><li>Home</li><li>Coffee</li><li>Shop</li><li>About Us</li><li>Imprint</li><li>Privacy</li></ul>
<ul class="abs f-list" style="left:681px;top:4450px"><li>Contact Us</li><li>Shopping Cart</li><li>Wishlist</li><li>FAQ</li><li>Shipping Policy</li></ul>
<ul class="abs f-list" style="left:921px;top:4450px"><li>Sign In</li><li>View Cart</li><li>Wishlist</li><li>FAQ</li></ul>

<div class="abs f-mark">Bohnwerk</div>
<div class="abs f-rule"></div>
<p class="abs copy">© 2019 Bohnwerk. All Rights Reserved.</p>
<div class="abs social" style="left:541px"></div>
<div class="abs social" style="left:589px"></div>
<div class="abs social" style="left:637px"></div>
<div class="abs social" style="left:685px"></div>
<div class="abs social" style="left:733px"></div>
<div class="abs social" style="left:781px"></div>
<div class="abs card" style="left:916px;background:#e8e8ee"></div>
<div class="abs card" style="left:968px;background:#7fb0d8"></div>
<div class="abs card" style="left:1020px;background:#d84a2a"></div>

</body>
</html>
```